Bref créative
The Marlowe Gala
Event Planning
Professional
Rosalind Hartwell
Owner - The Marlowe Gala
4105 - 27 Ashcombe Avenue
Toronto, ON M5R 2K7
rosalind@TheMarloweGala.example
www.TheMarloweGala.example
The card can be single or double sided i don't mind. Just be creative and make it clean!!!
Thanks!
It can be single or double sided I dont mind.

```html
<!DOCTYPE html>
<html lang="en">
<head>
<meta charset="UTF-8">
<title>The Marlowe Gala – Business Card</title>
<link rel="stylesheet" href="https://fonts.googleapis.com/css2?family=Open+Sans:wght@400;600;700&display=swap">
<style>
  :root {
    --page-bg: #e6e6e6;
    --card-dark-top: #5a5a5a;
    --card-dark-bottom: #3a3a3a;
    --card-light: #ffffff;
    --ink-dark: #3c3c3c;
    --ink-mid: #6a6a6a;
    --ink-light: #f2f2f2;
    --mark-grey: #6f6f6f;
    --tab-dark: #2e2e2e;
  }
  * { margin: 0; padding: 0; box-sizing: border-box; }
  html, body {
    width: 1200px; height: 901px; overflow: hidden;
    background: var(--page-bg);
    font-family: "Open Sans", Arial, sans-serif;
  }
  .stage {
    width: 1200px; height: 901px;
    display: flex; flex-direction: column;
    align-items: center; justify-content: center; gap: 56px;
  }
  .card {
    width: 660px; height: 377px; position: relative;
    box-shadow: 0 8px 24px rgba(0,0,0,.18);
    overflow: hidden;
  }

  /* Back side */
  .card-back {
    background: linear-gradient(160deg, var(--card-dark-top), var(--card-dark-bottom));
    color: var(--ink-light);
  }
  .back-mark {
    position: absolute; left: 50%; top: 50%;
    transform: translate(-50%, -50%);
    display: flex; align-items: center; gap: 18px;
  }
  .back-mark .mark-square {
    width: 54px; height: 54px; background: var(--ink-light);
  }
  .back-mark .mark-name {
    font-size: 30px; font-weight: 600; letter-spacing: 2px;
    text-transform: uppercase; color: var(--ink-light);
  }
  .back-url {
    position: absolute; right: 34px; top: 50%;
    transform: translateY(-50%) rotate(-90deg);
    transform-origin: center;
    font-size: 14px; letter-spacing: 1px; color: var(--ink-light);
    white-space: nowrap;
  }

  /* Front side */
  .card-front {
    background: var(--card-light); color: var(--ink-dark);
  }
  .brand {
    position: absolute; left: 40px; top: 34px;
  }
  .brand-row { display: flex; align-items: center; gap: 12px; }
  .brand .mark-square { width: 40px; height: 40px; background: var(--mark-grey); }
  .brand .mark-name {
    font-size: 22px; font-weight: 600; letter-spacing: 1.5px;
    text-transform: uppercase; color: var(--ink-dark);
  }
  .brand .tagline {
    margin: 4px 0 0 52px;
    font-size: 12px; letter-spacing: 3px; color: var(--ink-mid);
  }
  .address {
    position: absolute; left: 40px; top: 142px;
    font-size: 14px; line-height: 1.45; color: var(--ink-mid);
  }
  .contacts {
    position: absolute; left: 40px; top: 218px;
    list-style: none; font-size: 14px; line-height: 1.55; color: var(--ink-mid);
  }
  .contacts li { display: flex; align-items: center; gap: 8px; }
  .contacts svg { width: 13px; height: 13px; fill: var(--ink-mid); flex: none; }
  .person {
    position: absolute; right: 44px; top: 142px; text-align: left;
  }
  .person .name { font-size: 19px; font-weight: 600; color: var(--ink-dark); }
  .person .role { font-size: 13px; color: var(--ink-mid); margin-top: 2px; }
  .edge-tab {
    position: absolute; right: 0; top: 134px;
    width: 14px; height: 54px; background: var(--tab-dark);
  }
</style>
</head>
<body>
<main class="stage">
  <section class="card card-back" aria-label="Card back">
    <div class="back-mark">
      <span class="mark-square"></span>
      <span class="mark-name">The Marlowe Gala</span>
    </div>
    <p class="back-url">TheMarloweGala.example</p>
  </section>

  <section class="card card-front" aria-label="Card front">
    <div class="brand">
      <div class="brand-row">
        <span class="mark-square"></span>
        <span class="mark-name">The Marlowe Gala</span>
      </div>
      <p class="tagline">Event Planning</p>
    </div>

    <address class="address" style="font-style:normal">
      4105 - 27 Ashcombe Avenue<br>
      Toronto, ON M5R 2K7
    </address>

    <ul class="contacts">
      <li><svg viewBox="0 0 16 16"><path d="M3 1h3l1.5 4-2 1.2a9 9 0 0 0 4.3 4.3L11 8.5l4 1.5v3a2 2 0 0 1-2 2A13 13 0 0 1 1 3a2 2 0 0 1 2-2z"/></svg>416.555.0142</li>
      <li><svg viewBox="0 0 16 16"><rect x="4" y="1" width="8" height="14" rx="1.5"/></svg>416.555.0187</li>
      <li><svg viewBox="0 0 16 16"><rect x="2" y="6" width="12" height="8"/><rect x="4" y="2" width="8" height="4"/></svg>416.555.0163</li>
      <li><svg viewBox="0 0 16 16"><path d="M1 3h14v10H1z M1 3l7 6 7-6" fill="none" stroke="#6a6a6a" stroke-width="1.6"/></svg>rosalind@TheMarloweGala.example</li>
    </ul>

    <div class="person">
      <p class="name">Rosalind Hartwell</p>
      <p class="role">Owner - The Marlowe Gala</p>
    </div>
    <span class="edge-tab"></span>
  </section>
</main>
</body>
</html>
```